Design a Brochure...will hopefully lead to a full Website design

***UPDATED: There is a new Powerpoint that will outline a closer idea of what we are thinking for the back page of the brochure.

We are looking for a 2 page brochure ( Front and back, 1 piece of paper...2 sides) highlighting the services of our company, Vantor81.

We are truly looking for a web site designer, so we are using the brouche as a way to set the tone and feeling of the company, and then will hopefully be hiring the designer to build a fully functioning website (not e-commerce).

We will be having a dozen or so different brochures, handouts and presentations slides created over the 100 days. We are looking for someone who get what we are doing, and we can just work with and feed constant work. We are running this contest, to not have to run contests again.

I have included our logo, and a very very rough powerpoint layout and a word brochure outline. There are little to no graphics here. We are starting from the beginning, and setting the foundation for the entire website.

The colors of the company are Maroon and light grey.
The brochure will be printed on a high gloss finished paper-front and back

We believe that feelings are transferred through images, more than words. Words fill in some of the specifics, but they don't tell the story.

Vantor offers Track programs (maybe a race track like logo when referencing the programs) and individually catered Services (some kind of service logo)

* We will be giving lots of feedback for each design that comes anywhere near close to what we are thinking.

***Thank you in advance for your efforts!

The foundational Mindset of Vantor81

Vantor81 was started to teach the mindset and methodology for building a sustainable network of personal strategic partnerships and to provide the support and tools to implement the methodology. Our objective is to provide access to this "curriculum" via a variety of pathways from group trainings to individual coaching to keynotes. Most of our programming is tailored to the needs of the organization/individual leveraging our menu of skills training modules - from (i) teaching an associate how to become a client's trusted advisor to (ii) building an army of active advocates/recommendation sources to (iii) mastering planning and assessment.

By facilitating the discovery and adoption of an entrepreneurial mindset, we have seen people:

• take risks they never would have considered;
• turn to their strategic networks to solve problems faster and more efficiently that they would have tried to solve on their own; and
• shift from hoping for success to believing that their success is an inevitable result of applying the tools with purpose and accountability.

The founder and chief executive officer of VANTOR81, LLC has over twenty years of legal, marketing, product sales and business development experience with a proven track record in start-up law, high tech, B2B and B2C solution marketing and partnership development. Today, R focused on the development, implementation and expansion of VANTOR81’s Keystone Ladders – a step by step proprietary framework for teaching and applying best practices in relationship development and business sustainability. R provides advisor services to start-up and growth companies and executive coaching to entrepreneurs, lawyers and management consultants

```html
<!DOCTYPE html>
<html lang="en">
<head>
<meta charset="utf-8">
<title>Vantor81 Trifold Brochure</title>
<link href="https://fonts.googleapis.com/css2?family=Oswald:wght@300;500;700&family=Courier+Prime:wght@400;700&display=swap" rel="stylesheet">
<style>
  :root {
    --maroon: #6e1519;
    --maroon-deep: #4a0d10;
    --ink: #1b1b1d;
    --ink-soft: #2b2c2f;
    --paper: #ededed;
    --grey: #c9cccd;
    --stage: #d5d8d8;
    --white: #ffffff;
    --muted: #9a9c9f;
  }
  * { box-sizing: border-box; margin: 0; padding: 0; }
  html, body { width: 1200px; height: 800px; overflow: hidden; }
  body {
    background: var(--stage);
    font-family: "Courier Prime", monospace;
    display: flex; align-items: center; justify-content: center;
  }
  .brochure { display: flex; width: 1080px; height: 640px; box-shadow: 0 14px 40px rgba(0,0,0,.25); }
  .panel { width: 270px; height: 640px; position: relative; overflow: hidden; }

  /* Cover */
  .cover {
    background: linear-gradient(160deg, var(--maroon) 0%, var(--maroon-deep) 100%);
    color: var(--white); padding: 40px 28px;
    display: flex; flex-direction: column; justify-content: space-between;
  }
  .brand { display: flex; align-items: center; gap: 12px; }
  .brand-mark { width: 26px; height: 26px; border: 2px solid var(--white); }
  .brand-name { font-family: "Oswald", sans-serif; font-weight: 300; font-size: 34px; letter-spacing: 3px; }
  .motto {
    font-family: "Oswald", sans-serif; font-weight: 700; font-size: 19px;
    line-height: 1.25; text-transform: uppercase; letter-spacing: .5px;
  }

  /* Shared photo strip */
  .photo {
    height: 120px;
    background: linear-gradient(180deg, #b9c4cc 0%, #e9eef1 55%, #8d969c 100%);
  }
  .photo--dark { background: linear-gradient(180deg, #8f9aa2 0%, #3a3d41 70%, #1f2022 100%); }

  /* Dark panels */
  .services, .company { background: linear-gradient(180deg, var(--ink-soft), var(--ink)); color: var(--white); }
  .band {
    background: var(--maroon); color: var(--white);
    font-family: "Oswald", sans-serif; font-weight: 500; font-size: 15px;
    letter-spacing: 2px; text-transform: uppercase; padding: 7px 18px;
    border-top: 3px solid var(--grey);
  }
  .services-body { padding: 16px 20px; font-size: 10.5px; line-height: 1.45; text-transform: uppercase; }
  .services-body h3 {
    font-family: "Oswald", sans-serif; font-weight: 500; font-size: 13px;
    letter-spacing: 1px; margin: 12px 0 4px; color: var(--grey);
  }
  .services-body ul { list-style: none; }
  .services-body li::before { content: "› "; color: var(--maroon); }
  .services-body p { margin-top: 6px; }

  .section-title {
    font-family: "Oswald", sans-serif; font-weight: 500; font-size: 13px;
    letter-spacing: 1px; text-transform: uppercase; padding: 12px 18px 6px;
  }
  .company .section-title { color: var(--white); }
  .track-list { list-style: none; padding: 0 14px; }
  .track {
    display: grid; grid-template-columns: 44px 1fr; gap: 10px;
    padding: 8px 0; border-bottom: 1px solid rgba(255,255,255,.25);
  }
  .track h4 {
    font-family: "Oswald", sans-serif; font-weight: 500; font-size: 11px;
    letter-spacing: 1px; text-transform: uppercase; margin-bottom: 2px;
  }
  .track p { font-size: 8.6px; line-height: 1.35; }
  .icon { width: 42px; height: 42px; }

  /* Light panel */
  .individual { background: var(--paper); color: var(--ink); }
  .individual .section-title { color: var(--maroon); text-align: right; }
  .individual .track {
    grid-template-columns: 1fr 44px; border-bottom: 1px solid var(--grey);
    border-right: 2px solid var(--maroon); padding-right: 10px;
  }
  .individual .track h4 { color: var(--maroon); text-align: right; }
  .individual .track p { text-align: right; }
</style>
</head>
<body>
<main class="brochure">

  <section class="panel cover">
    <div class="brand">
      <span class="brand-mark"></span>
      <span class="brand-name">VANTOR81</span>
    </div>
    <p class="motto">Growth is the objective.<br>If the direction is clear,<br>the assessment is sound,<br>the planning is true<br>and the execution is purposeful,<br>the desired result is inevitable</p>
  </section>

  <section class="panel services">
    <div class="photo photo--dark" role="img" aria-label="Dark mountain ridge under an overcast sky"></div>
    <div class="band">Program Track</div>
    <div class="services-body">
      <h3>Services</h3>
      <ul>
        <li>Business Development</li>
        <li>Any Company Size</li>
        <li>Strategic Plan</li>
        <li>Growth Metrics</li>
        <li>Team Strategies</li>
      </ul>
      <h3>Individual Coaching</h3>
      <ul>
        <li>Executive Review</li>
        <li>Group Sessions</li>
      </ul>
      <h3>Keynote Events:</h3>
      <ul><li>Take your staff away</li></ul>
      <p>Whether you need to spark passion or to introduce new tools to your staff and partners, or are looking for a motivational keynote from an expert in sales, communication and motivation, we can help.</p>
    </div>
  </section>

  <section class="panel company">
    <div class="photo photo--dark" role="img" aria-label="Snow-covered mountain slope fading into dark sky"></div>
    <h2 class="section-title">Company Vantor Tracks</h2>
    <ul class="track-list">
      <li class="track">
        <svg class="icon" viewBox="0 0 42 42" fill="none" stroke="#fff" stroke-width="2"><circle cx="21" cy="21" r="19"/><rect x="12" y="13" width="12" height="6" transform="rotate(-35 18 16)" fill="#fff"/><line x1="20" y1="19" x2="28" y2="29"/><line x1="11" y1="31" x2="25" y2="31"/></svg>
        <div><h4>Associate to Partner</h4><p>Lorem ipsum dolor sit amet, consectetur adipiscing elit, sed do eiusmod tempor incididunt ut labore et dolore magna aliqua. Ut enim ad minim veniam, quis nostrud exercitation ullamco laboris nisi ut aliquip ex ea commodo.</p></div>
      </li>
      <li class="track">
        <svg class="icon" viewBox="0 0 42 42" fill="none" stroke="#fff" stroke-width="2"><circle cx="21" cy="21" r="19"/><rect x="11" y="16" width="8" height="14" fill="#fff"/><rect x="20" y="11" width="10" height="19" fill="#fff"/></svg>
        <div><h4>Organizational Training</h4><p>Lorem ipsum dolor sit amet, consectetur adipiscing elit, sed do eiusmod tempor incididunt ut labore et dolore magna aliqua. Ut enim ad minim veniam, quis nostrud exercitation ullamco laboris nisi ut aliquip ex ea commodo.</p></div>
      </li>
      <li class="track">
        <svg class="icon" viewBox="0 0 42 42" fill="none" stroke="#fff" stroke-width="2"><circle cx="21" cy="21" r="19"/><circle cx="15" cy="17" r="3" fill="#fff"/><circle cx="27" cy="17" r="3" fill="#fff"/><path d="M9 29 q6 -9 12 0 q6 -9 12 0" fill="#fff"/></svg>
        <div><h4>Keynote Speaking</h4><p>Lorem ipsum dolor sit amet, consectetur adipiscing elit, sed do eiusmod tempor incididunt ut labore et dolore magna aliqua. Ut enim ad minim veniam, quis nostrud exercitation ullamco laboris nisi ut aliquip ex ea commodo.</p></div>
      </li>
      <li class="track">
        <svg class="icon" viewBox="0 0 42 42" fill="none" stroke="#fff" stroke-width="2"><circle cx="21" cy="21" r="19"/><rect x="12" y="24" width="4" height="7" fill="#fff"/><rect x="19" y="20" width="4" height="11" fill="#fff"/><rect x="26" y="15" width="4" height="16" fill="#fff"/><polyline points="11,20 18,15 23,17 31,10"/></svg>
        <div><h4>Distribution &amp; Sales</h4><p>Lorem ipsum dolor sit amet, consectetur adipiscing elit, sed do eiusmod tempor incididunt ut labore et dolore magna aliqua. Ut enim ad minim veniam, quis nostrud exercitation ullamco laboris nisi ut aliquip ex ea commodo.</p></div>
      </li>
    </ul>
  </section>

  <section class="panel individual">
    <div class="photo" role="img" aria-label="Bright snowy mountain peak against a pale sky"></div>
    <h2 class="section-title">Individual Vantor Tracks</h2>
    <ul class="track-list">
      <li class="track">
        <div><h4>Recovery Vantor</h4><p>Lorem ipsum dolor sit amet, consectetur adipiscing elit, sed do eiusmod tempor incididunt ut labore et dolore magna aliqua. Ut enim ad minim veniam, quis nostrud exercitation ullamco.</p></div>
        <svg class="icon" viewBox="0 0 42 42" fill="none" stroke="#1b1b1d" stroke-width="2"><circle cx="21" cy="21" r="19"/><path d="M29 17 a9 9 0 1 0 1 8"/><polyline points="29,11 29,17 23,17"/></svg>
      </li>
      <li class="track">
        <div><h4>Transitional Vantor</h4><p>Lorem ipsum dolor sit amet, consectetur adipiscing elit, sed do eiusmod tempor incididunt ut labore et dolore magna aliqua. Ut enim ad minim veniam, quis nostrud exercitation ullamco.</p></div>
        <svg class="icon" viewBox="0 0 42 42" fill="none" stroke="#1b1b1d" stroke-width="2"><circle cx="21" cy="21" r="19"/><line x1="12" y1="30" x2="30" y2="12"/><line x1="12" y1="12" x2="30" y2="30"/><polyline points="24,12 30,12 30,18"/><polyline points="24,30 30,30 30,24"/></svg>
      </li>
      <li class="track">
        <div><h4>Entrepreneurial Vantor</h4><p>Lorem ipsum dolor sit amet, consectetur adipiscing elit, sed do eiusmod tempor incididunt ut labore et dolore magna aliqua. Ut enim ad minim veniam, quis nostrud exercitation ullamco.</p></div>
        <svg class="icon" viewBox="0 0 42 42" fill="none" stroke="#1b1b1d" stroke-width="2"><circle cx="21" cy="21" r="19"/><circle cx="21" cy="16" r="4" fill="#1b1b1d"/><path d="M13 31 q8 -14 16 0" fill="#1b1b1d"/></svg>
      </li>
      <li class="track">
        <div><h4>Momentum Vantor</h4><p>Lorem ipsum dolor sit amet, consectetur adipiscing elit, sed do eiusmod tempor incididunt ut labore et dolore magna aliqua. Ut enim ad minim veniam, quis nostrud exercitation ullamco.</p></div>
        <svg class="icon" viewBox="0 0 42 42" fill="none" stroke="#1b1b1d" stroke-width="1.6"><circle cx="21" cy="21" r="19"/><line x1="11" y1="12" x2="31" y2="12"/><line x1="15" y1="12" x2="11" y2="24"/><line x1="19" y1="12" x2="19" y2="26"/><line x1="23" y1="12" x2="23" y2="26"/><line x1="27" y1="12" x2="27" y2="26"/><circle cx="11" cy="26" r="2.5" fill="#1b1b1d"/><circle cx="19" cy="28" r="2.5" fill="#1b1b1d"/><circle cx="23" cy="28" r="2.5" fill="#1b1b1d"/><circle cx="27" cy="28" r="2.5" fill="#1b1b1d"/></svg>
      </li>
    </ul>
  </section>

</main>
</body>
</html>
```